Business Card Design for a Design/Build Firm

Harrowgate Structures Group, Inc. is a firm providing construction professional project management and architectural design services to an international clientele. Contemporary. "Green" movement aware. Business card to have back design/logo. Cards will be on high gloss paper

Target Market(s)

Building Developers and Owners

Industry/Entity Type

Construction

Requirements
Nice to have
• We really would like to use the acronym "HSG" as main focal point fo card design. Company will be known as HSG.
Should not have
• No globes or abstract images of buildings.

```html
<!DOCTYPE html>
<html lang="en">
<head>
<meta charset="utf-8">
<title>HSG Business Card</title>
<link href="https://fonts.googleapis.com/css2?family=Poppins:wght@200;800&family=Questrial&display=swap" rel="stylesheet">
<style>
  :root {
    --teal-light: #4f8683;
    --teal-mid: #386462;
    --teal-dark: #1e3333;
    --ink: #ffffff;
    --ghost: rgba(70, 78, 80, 0.38);
    --edge: #8fb0ae;
  }
  html, body {
    margin: 0;
    padding: 0;
    width: 1200px;
    height: 675px;
    overflow: hidden;
    background: #ffffff;
  }
  .card {
    position: relative;
    width: 1200px;
    height: 675px;
    box-sizing: border-box;
    border: 1px solid var(--edge);
    overflow: hidden;
    background: radial-gradient(ellipse 75% 95% at 28% 62%, var(--teal-light) 0%, var(--teal-mid) 50%, var(--teal-dark) 100%);
  }
  .brand-ghost {
    position: absolute;
    left: 70px;
    top: -120px;
    margin: 0;
    font-family: "Poppins", sans-serif;
    font-weight: 200;
    font-size: 560px;
    line-height: 1;
    letter-spacing: 10px;
    color: var(--ghost);
    white-space: nowrap;
  }
  .brand-mark {
    position: absolute;
    left: 222px;
    top: 92px;
    margin: 0;
    font-family: "Poppins", sans-serif;
    font-weight: 200;
    font-size: 200px;
    line-height: 1;
    color: var(--ink);
    white-space: nowrap;
  }
  .company-name {
    position: absolute;
    left: 228px;
    top: 310px;
    margin: 0;
    font-family: "Poppins", sans-serif;
    font-weight: 800;
    font-size: 44px;
    line-height: 1;
    letter-spacing: 0.5px;
    color: var(--ink);
    white-space: nowrap;
  }
  .contact {
    position: absolute;
    left: 77px;
    top: 434px;
    margin: 0;
    font-family: "Questrial", sans-serif;
    color: var(--ink);
  }
  .contact-name {
    display: block;
    font-size: 48px;
    line-height: 1;
    margin-bottom: 12px;
  }
  .contact-line {
    display: block;
    font-size: 34px;
    line-height: 48px;
  }
</style>
</head>
<body>
  <div class="card">
    <p class="brand-ghost" aria-hidden="true">HSG</p>
    <p class="brand-mark">HSG</p>
    <h1 class="company-name">Harrowgate Structures Group</h1>
    <address class="contact">
      <span class="contact-name">Your Name Here</span>
      <span class="contact-line">Title will be here</span>
      <span class="contact-line">Harrowgate Structures Group</span>
      <span class="contact-line">Ph: +0123456789 - web. www.harrowgatesg.com</span>
    </address>
  </div>
</body>
</html>
```